Cross Country Transportation and Logistics Company need a Business Card Design

We need a business Card Design for a company based in Singapore, We had offices in Malaysia, Bangkok, Vietnam and China. Our Core business is cross border trucking to and from Singapore, Malaysia and Thailand. Our service also include event logistics, show moves and freight forwarding services. We made logistics possible is the region of Intra Asia.

Detail of the company as below.
Company Name: ORBEX FREIGHT (S) PTE LTD
Company Registration Number: 208867392K
Address: 14 Tuas Berry Industrial Way 3C #05-22 TBW Cargohub Singapore 539284
Office: +65 62418397
Fax: +65 62418764
Webiste: www.orbexfreight.example.sg

Business Card holder as below:
Name: Marcus Teo
Position: Director
Mobile: +65 9847 1156
Email: marcus.teo@orbexfreight.example.sg

Name: Clara Seah
Position: Finance Manager
Mobile: +65 9312 8840
Email: clara.seah@orbexfreight.example.sg

Name: Derek Koh
Position: General Manager
Mobile: +6016 584 3927
Email: derek.koh@orbexfreight.example.sg

Target Market(s)

I am targeting on the electronic component manufacturer and their freight to transport from Singapore to Malaysia and Thailand r vice verse.

Industry/Entity Type

Freight Forwarding

Requirements
Must have
• We make logistics possible

```html
<!DOCTYPE html>
<html lang="en">
<head>
<meta charset="utf-8">
<title>Orbex Freight – Business Card</title>
<link href="https://fonts.googleapis.com/css2?family=Open+Sans:wght@400;600;700&display=swap" rel="stylesheet">
<style>
  :root {
    --backdrop: #e7e4df;
    --card-light: #ffffff;
    --card-shade: #dcdde0;
    --navy: #1c2f7a;
    --accent: #3f3f9c;
    --logo-grey: #8e9ab5;
    --ink: #4a4a52;
    --on-accent: #ffffff;
  }
  * { box-sizing: border-box; margin: 0; padding: 0; }
  html, body { width: 1200px; height: 894px; overflow: hidden; }
  body {
    background: var(--backdrop);
    font-family: "Open Sans", Arial, sans-serif;
    position: relative;
  }
  .card {
    position: absolute;
    top: 177px;
    width: 330px;
    height: 540px;
    border-radius: 18px;
    overflow: hidden;
    background: radial-gradient(ellipse at 45% 40%, var(--card-light) 0%, var(--card-shade) 100%);
    box-shadow: 0 10px 26px rgba(0,0,0,0.18);
  }
  .card--front { left: 230px; }
  .card--back { left: 640px; }

  .brand {
    display: flex;
    align-items: center;
    gap: 10px;
    color: var(--navy);
    font-weight: 700;
    letter-spacing: 0.05em;
    white-space: nowrap;
  }
  .brand__dot {
    border-radius: 50%;
    background: var(--logo-grey);
    flex: none;
  }

  .front-lockup {
    position: absolute;
    left: 0; right: 0; top: 50%;
    transform: translateY(-50%);
    display: flex;
    flex-direction: column;
    align-items: center;
    gap: 14px;
  }
  .card--front .brand { font-size: 25px; }
  .card--front .brand__dot { width: 34px; height: 34px; }
  .tagline {
    color: var(--accent);
    font-size: 12px;
    font-weight: 600;
    letter-spacing: 0.12em;
    text-transform: uppercase;
  }

  .card--back .brand {
    position: absolute;
    left: 26px; top: 36px;
    font-size: 21px;
  }
  .card--back .brand__dot { width: 28px; height: 28px; }

  .name-tab {
    position: absolute;
    left: 0; top: 104px;
    width: 250px; height: 56px;
    background: var(--accent);
    border-radius: 0 28px 28px 0;
    color: var(--on-accent);
    padding: 8px 0 0 26px;
  }
  .name-tab__name { font-size: 19px; font-weight: 700; letter-spacing: 0.04em; line-height: 1.1; }
  .name-tab__role { font-size: 11px; letter-spacing: 0.08em; }

  .contacts {
    position: absolute;
    left: 26px; right: 16px; top: 190px;
    list-style: none;
    color: var(--ink);
    font-size: 10.5px;
    letter-spacing: 0.02em;
  }
  .contacts__item {
    display: flex;
    align-items: flex-start;
    gap: 9px;
    line-height: 15px;
    margin-bottom: 10px;
  }
  .contacts__icon { width: 15px; height: 15px; flex: none; }

  .card--back .tagline {
    position: absolute;
    left: 26px; bottom: 50px;
    font-size: 11px;
  }

  .base-band {
    position: absolute;
    left: 0; right: 0; bottom: 0;
    height: 26px;
    background: var(--accent);
  }
</style>
</head>
<body>

  <section class="card card--front" aria-label="Business card front">
    <div class="front-lockup">
      <div class="brand"><span class="brand__dot"></span>ORBEX FREIGHT</div>
      <p class="tagline">We make logistics possible</p>
    </div>
  </section>

  <section class="card card--back" aria-label="Business card back">
    <div class="brand"><span class="brand__dot"></span>ORBEX FREIGHT</div>

    <div class="name-tab">
      <p class="name-tab__name">DEREK KOH</p>
      <p class="name-tab__role">GENERAL MANAGER</p>
    </div>

    <ul class="contacts">
      <li class="contacts__item">
        <svg class="contacts__icon" viewBox="0 0 16 16"><circle cx="8" cy="8" r="7.5" fill="var(--accent)"/><rect x="5.5" y="4" width="5" height="8" rx="1" fill="none" stroke="#fff" stroke-width="1.2"/></svg>
        <span>+65 62418397</span>
      </li>
      <li class="contacts__item">
        <svg class="contacts__icon" viewBox="0 0 16 16"><circle cx="8" cy="8" r="7.5" fill="var(--accent)"/><path d="M5 4.5c0 4 2.5 6.5 6.5 6.5l.5-1.6-1.8-.8-.9.9c-1-.5-2-1.5-2.5-2.5l.9-.9-.8-1.8z" fill="#fff"/></svg>
        <span>+6016 584 3927</span>
      </li>
      <li class="contacts__item">
        <svg class="contacts__icon" viewBox="0 0 16 16"><circle cx="8" cy="8" r="7.5" fill="var(--accent)"/><circle cx="8" cy="8" r="1.8" fill="none" stroke="#fff" stroke-width="1.2"/><path d="M9.8 8v1c0 1.5 2 1.5 2 0V8a3.8 3.8 0 1 0-1.5 3" fill="none" stroke="#fff" stroke-width="1.2"/></svg>
        <span>DEREK.KOH@ORBEXFREIGHT.EXAMPLE.SG</span>
      </li>
      <li class="contacts__item">
        <svg class="contacts__icon" viewBox="0 0 16 16"><circle cx="8" cy="8" r="7.5" fill="var(--accent)"/><circle cx="8" cy="8" r="4" fill="none" stroke="#fff" stroke-width="1"/><ellipse cx="8" cy="8" rx="1.7" ry="4" fill="none" stroke="#fff" stroke-width="1"/><path d="M4 8h8" stroke="#fff" stroke-width="1"/></svg>
        <span>WWW.ORBEXFREIGHT.EXAMPLE.SG</span>
      </li>
      <li class="contacts__item">
        <svg class="contacts__icon" viewBox="0 0 16 16"><circle cx="8" cy="8" r="7.5" fill="var(--accent)"/><path d="M8 12.5s-3-3.3-3-5.5a3 3 0 0 1 6 0c0 2.2-3 5.5-3 5.5z" fill="#fff"/><circle cx="8" cy="7" r="1.1" fill="var(--accent)"/></svg>
        <span>14 TUAS BERRY INDUSTRIAL WAY 3C,<br>SINGAPORE 539284</span>
      </li>
    </ul>

    <p class="tagline">We make logistics possible</p>

    <div class="base-band"></div>
  </section>

</body>
</html>
```